Beacon Law Stationary - Law Firm

I am looking for a designer who can help me design letterhead and envelopes consistent with our new business cards. Feel free to reach out to me directly at ned@beaconlawgroup.example. Thank you!! Visit beaconlawgroup.example to see our site and the attached files for creative assets.

Target Market(s)

Anyone needing a lawyer

Font styles to use
Other font styles liked:
• Adobe Caslon Pro

Requirements
Must have
• Adobe Caslon Pro font
Full color
Nice to have
• My photo on front along with 2/3 face of camo - see mock up for example of what I have in mind.

American colors - similar to the ones found on my website and gold.

```html
<!DOCTYPE html>
<html lang="en">
<head>
<meta charset="utf-8">
<title>Beacon Law Stationery</title>
<link rel="stylesheet" href="https://fonts.googleapis.com/css2?family=Libre+Caslon+Text:ital,wght@0,400;0,700;1,400&family=Crimson+Pro:wght@400;600&display=swap">
<style>
  :root {
    --navy: #001b42;
    --gold-1: #f7d566;
    --gold-2: #f6efc6;
    --gold-3: #c59c38;
    --gold-text: #e6c25e;
    --heading-blue: #1d4f8e;
    --ink: #2a2a2a;
    --backdrop: #a6a6a6;
    --paper: #ffffff;
    --photo-dark: #1a1c22;
    --photo-light: #e9e9ea;
    --faint-mark: #ececed;
  }
  * { box-sizing: border-box; margin: 0; padding: 0; }
  html, body { width: 707px; height: 1200px; overflow: hidden; }
  body { background: var(--backdrop); position: relative; font-family: "Crimson Pro", Georgia, serif; color: var(--ink); }

  .letterhead { position: absolute; left: 81px; top: 80px; width: 544px; height: 703px; background: var(--paper); overflow: hidden; }
  .letterhead-header { position: absolute; left: 0; top: 0; width: 544px; height: 66px; }
  .letterhead-header svg { position: absolute; left: 0; top: 0; }
  .firm-name { position: absolute; font-family: "Libre Caslon Text", Georgia, serif; letter-spacing: 1.5px; white-space: nowrap; }
  .brand-dot { position: absolute; left: 30px; top: 18px; width: 22px; height: 22px; border-radius: 50%; border: 1.5px solid var(--gold-text); }
  .letterhead .firm-name { left: 64px; top: 20px; font-size: 16px; color: var(--gold-text); }
  .mission { position: absolute; right: 32px; top: 41px; font-family: "Libre Caslon Text", Georgia, serif; font-style: italic; font-size: 13px; color: var(--navy); white-space: nowrap; }

  .date-line { position: absolute; right: 55px; top: 90px; font-size: 10.5px; }
  .date-line span { display: inline-block; width: 70px; border-bottom: 0.7px solid var(--ink); margin-left: 3px; }

  .letter-body { position: absolute; left: 41px; top: 134px; width: 460px; font-size: 10.6px; }
  .letter-body p { line-height: 18.2px; white-space: nowrap; }
  .section-title { font-family: "Libre Caslon Text", Georgia, serif; font-weight: 700; font-size: 9.6px; margin-top: 13px; line-height: 14px; color: #111; }
  .section-title.takeaways { color: var(--heading-blue); letter-spacing: -0.2px; margin-top: 14px; }
  .section-title + p { margin-top: 2px; }
  .checklist { list-style: none; margin-top: 5px; }
  .checklist li { position: relative; padding-left: 21px; line-height: 15.7px; white-space: nowrap; }
  .checklist.spaced li { line-height: 17.5px; }
  .checklist svg { position: absolute; left: 0; top: 4px; width: 10px; height: 9px; }
  .gap-after-title { margin-top: 9px !important; }

  .letterhead-footer { position: absolute; left: 0; top: 643px; width: 544px; height: 60px; }
  .letterhead-footer svg { position: absolute; left: 0; top: 0; }
  .footer-contact { position: absolute; left: 0; width: 100%; text-align: center; font-family: "Libre Caslon Text", Georgia, serif; white-space: nowrap; }
  .footer-contact.primary { top: 22px; font-size: 10px; color: #fff; }
  .footer-contact.practice { top: 39px; font-size: 9px; color: var(--gold-text); }
  .footer-contact svg { position: static; display: inline-block; vertical-align: -1px; }

  .envelope { position: absolute; left: 81px; top: 833px; width: 544px; height: 234px; background: var(--paper); overflow: hidden; }
  .envelope svg.env-shapes { position: absolute; left: 0; top: 0; }
  .attorney-photo { position: absolute; left: 0; top: 4px; width: 154px; height: 230px; background: linear-gradient(180deg, var(--photo-light) 0%, #c9c9cc 22%, var(--photo-dark) 40%, var(--photo-dark) 100%); }
  .envelope .firm-name { left: 162px; width: 210px; text-align: center; top: 13px; font-size: 22px; color: var(--navy); letter-spacing: 2px; }
  .envelope-address { position: absolute; left: 162px; width: 210px; text-align: center; top: 40px; font-family: "Libre Caslon Text", Georgia, serif; font-size: 9.5px; color: var(--navy); white-space: nowrap; }
  .envelope-mark { position: absolute; left: 421px; top: 40px; width: 120px; text-align: center; }
  .envelope-mark .mark-circle { width: 84px; height: 84px; margin: 0 auto; border-radius: 50%; border: 3px solid var(--faint-mark); }
  .envelope-mark .mark-name { margin-top: 10px; font-family: "Libre Caslon Text", Georgia, serif; font-size: 13px; letter-spacing: 1.5px; color: var(--faint-mark); white-space: nowrap; }
  .envelope-tagline { position: absolute; left: 160px; width: 384px; top: 211px; text-align: center; font-family: "Libre Caslon Text", Georgia, serif; font-weight: 700; font-size: 11px; color: var(--gold-text); white-space: nowrap; }
  .envelope-tagline .divider { margin: 0 14px; font-weight: 400; }
</style>
</head>
<body>
<svg width="0" height="0" style="position:absolute">
  <defs>
    <linearGradient id="goldSweep" x1="0" y1="0" x2="1" y2="0">
      <stop offset="0" stop-color="#f7d566"/>
      <stop offset="0.3" stop-color="#f6efc6"/>
      <stop offset="0.6" stop-color="#c59c38"/>
      <stop offset="1" stop-color="#f6efc6"/>
    </linearGradient>
    <symbol id="tick-box" viewBox="0 0 10 9">
      <rect x="0.6" y="1.4" width="7" height="7" rx="1" fill="none" stroke="#001b42" stroke-width="1.1"/>
      <path d="M2.2 4.6 L4 6.4 L9.4 0.8" fill="none" stroke="#001b42" stroke-width="1.6"/>
    </symbol>
  </defs>
</svg>

<section class="letterhead">
  <header class="letterhead-header">
    <svg width="544" height="66" viewBox="0 0 544 66">
      <rect x="0" y="0" width="544" height="61" fill="#001b42"/>
      <rect x="0" y="61" width="230" height="4" fill="url(#goldSweep)"/>
      <polygon points="247,35 544,35 544,65 225,65" fill="url(#goldSweep)"/>
      <polygon points="220,61 228,61 250,35 242,35" fill="url(#goldSweep)"/>
      <polygon points="231,61 239,61 261,35 253,35" fill="url(#goldSweep)"/>
    </svg>
    <div class="brand-dot"></div>
    <div class="firm-name">BEACON LAW</div>
    <div class="mission">Our Mission: To Fight and Win for You.</div>
  </header>

  <div class="date-line">Date:<span></span></div>

  <main class="letter-body">
    <p>Lorem Ipsum is simply dummy text of the printing and typesetting industry. Lorem Ipsum has been the<br>industry's standard dummy text ever since the 1500s, when an unknown printer took a galley of type and<br>scrambled it to make a type specimen book. It has survived not only five centuries, but also the leap into</p>

    <h2 class="section-title takeaways">KEY TAKEAWAYS</h2>
    <p>Lorem Ipsum is simply dummy text of the printing and typesetting industry. Lorem Ipsum has been</p>
    <ul class="checklist">
      <li><svg><use href="#tick-box"/></svg>Lorem Ipsum is simply</li>
      <li><svg><use href="#tick-box"/></svg>Lorem Ipsum is simply</li>
      <li><svg><use href="#tick-box"/></svg>Lorem Ipsum is simply</li>
    </ul>

    <h2 class="section-title">Initial Access</h2>
    <p>Lorem Ipsum is simply dummy text of the printing and typesetting industry. Lorem Ipsum has been the<br>industry's standard dummy text ever since the 1500s, when an unknown printer took a galley of type and<br>scrambled it to make a type specimen book. It has survived not only five centuries, but also the leap into</p>

    <h2 class="section-title">Execution</h2>
    <p>Lorem Ipsum is simply dummy text of the printing and</p>
    <ul class="checklist">
      <li><svg><use href="#tick-box"/></svg>Lorem Ipsum is simply</li>
      <li><svg><use href="#tick-box"/></svg>Lorem Ipsum is simply</li>
      <li><svg><use href="#tick-box"/></svg>Lorem Ipsum is simply</li>
    </ul>

    <h2 class="section-title">Capabilties</h2>
    <p class="gap-after-title">Lorem Ipsum is simply dummy text of the printing and</p>
    <ul class="checklist spaced">
      <li><svg><use href="#tick-box"/></svg>Lorem Ipsum is simply dummy text of the printing and typesetting industry. Lorem Ipsum</li>
      <li><svg><use href="#tick-box"/></svg>Lorem Ipsum is simply dummy text of the</li>
      <li><svg><use href="#tick-box"/></svg>Lorem Ipsum is simply dummy text of the printing and typesetting industry.<br>Lorem Ipsum has been the industry's standard dummy text ever since the<br>1500s, when an unknown printer took a galley of type and scrambled it to</li>
    </ul>
  </main>

  <footer class="letterhead-footer">
    <svg width="544" height="60" viewBox="0 0 544 60">
      <polygon points="0,4 346,4 337,12 0,12" fill="url(#goldSweep)"/>
      <polygon points="361,0 544,0 544,60 0,60 0,15 342,15" fill="#001b42"/>
    </svg>
    <div class="footer-contact primary">Beacon Law |
      <svg width="7" height="9" viewBox="0 0 7 9"><path d="M3.5 0.5 A3 3 0 0 1 6.5 3.5 C6.5 5.5 3.5 8.6 3.5 8.6 C3.5 8.6 0.5 5.5 0.5 3.5 A3 3 0 0 1 3.5 0.5 Z M3.5 2.3 A1.2 1.2 0 1 0 3.5 4.7 A1.2 1.2 0 1 0 3.5 2.3 Z" fill="#fff" fill-rule="evenodd"/></svg>
      48 Harbor Lane, Fairview, Ohio 44012 |
      <svg width="8" height="8" viewBox="0 0 8 8"><path d="M1.5 0.5 L3 0.5 L3.6 2.3 L2.7 3 C3.2 4.1 3.9 4.8 5 5.3 L5.7 4.4 L7.5 5 L7.5 6.5 C7.5 7.1 7 7.5 6.4 7.5 C3.4 7.2 0.8 4.6 0.5 1.6 C0.5 1 0.9 0.5 1.5 0.5 Z" fill="#fff"/></svg>
      (555) 014-2290</div>
    <div class="footer-contact practice">Auto Accidents | Personal Injury | Criminal Defense | Injunctions | Victim Representation | Family Law</div>
  </footer>
</section>

<section class="envelope">
  <svg class="env-shapes" width="544" height="234" viewBox="0 0 544 234">
    <polygon points="0,0 394,0 355,64 0,64" fill="url(#goldSweep)"/>
    <polygon points="400,0 415,0 373,64 357,64" fill="#001b42"/>
    <polygon points="418,0 433,0 391,64 376,64" fill="#001b42"/>
    <polygon points="196,201 544,201 544,234 154,234" fill="#001b42"/>
  </svg>
  <div class="attorney-photo" role="img" aria-label="Portrait photo of the attorney in a dark suit and blue tie"></div>
  <div class="firm-name">BEACON LAW</div>
  <div class="envelope-address">48 Harbor Lane, Fairview, Ohio 44012</div>
  <div class="envelope-mark">
    <div class="mark-circle"></div>
    <div class="mark-name">BEACON LAW</div>
  </div>
  <div class="envelope-tagline">beaconlawgroup.example<span class="divider">|</span>A VETERAN OWNED LAW FIRM</div>
</section>
</body>
</html>
```